Packaging design for a low carb bar

I am producing a low carb / high fat bar, therefore I would like to have a light weighted modern design. The background color pastel light or something like that. The package should be focused on fitness-active individuals who are looking for healthy low carb snacks. Preliminary packaging size, logo, and more details on what should be attached to the packaging are attached. Thank you!

```html
<!DOCTYPE html>
<html lang="en">
<head>
<meta charset="utf-8">
<title>Keto Bar Packaging</title>
<link rel="stylesheet" href="https://fonts.googleapis.com/css2?family=Antonio:wght@200&family=Montserrat:wght@400;600;700&family=Marcellus+SC&display=swap">
<style>
  :root {
    --backdrop: #d9a6cf;
    --sky: #a7d4e7;
    --ocean: #65b1cf;
    --ocean-deep: #57a5c6;
    --teal: #3f98a3;
    --teal-soft: #62b3bd;
    --paper: #f1f2f4;
    --paper-shade: #e2e4e7;
    --plum: #7b4f92;
    --white: #ffffff;
  }
  html, body { margin: 0; padding: 0; overflow: hidden; }
  body {
    width: 1200px; height: 1200px;
    background: var(--backdrop);
    display: flex; align-items: center; justify-content: center;
  }
  .pack { width: 560px; height: 1100px; display: block; box-shadow: 0 10px 30px rgba(80,30,80,.25); }
  .brand-name { font-family: "Montserrat", sans-serif; font-weight: 400; fill: var(--white); font-size: 34px; letter-spacing: 5px; }
  .product-title { font-family: "Antonio", sans-serif; font-weight: 200; fill: var(--white); font-size: 170px; }
  .claim { font-family: "Montserrat", sans-serif; font-weight: 600; fill: var(--white); font-size: 21px; }
  .section-label { font-family: "Montserrat", sans-serif; font-weight: 700; fill: var(--teal); font-size: 20px; letter-spacing: 1px; }
  .ingredient-label { font-family: "Montserrat", sans-serif; font-weight: 700; fill: var(--white); font-size: 11px; }
  .flavour { font-family: "Marcellus SC", serif; fill: var(--plum); font-size: 36px; }
</style>
</head>
<body>
<svg class="pack" viewBox="0 0 560 1100" xmlns="http://www.w3.org/2000/svg">
  <defs>
    <linearGradient id="sky-fade" x1="0" y1="0" x2="0" y2="1">
      <stop offset="0" stop-color="var(--sky)"/>
      <stop offset="1" stop-color="#94c9e0"/>
    </linearGradient>
    <linearGradient id="ocean-fade" x1="0" y1="0" x2="0" y2="1">
      <stop offset="0" stop-color="var(--ocean)"/>
      <stop offset="1" stop-color="var(--ocean-deep)"/>
    </linearGradient>
    <linearGradient id="paper-fade" x1="0" y1="0" x2="0" y2="1">
      <stop offset="0" stop-color="var(--paper)"/>
      <stop offset="1" stop-color="var(--paper-shade)"/>
    </linearGradient>
  </defs>

  <rect class="panel-top" x="0" y="0" width="560" height="1100" fill="url(#sky-fade)"/>
  <rect class="panel-bottom" x="0" y="700" width="560" height="400" fill="url(#paper-fade)"/>
  <rect class="colour-wash" x="30" y="200" width="500" height="640" fill="url(#ocean-fade)"
        role="img" aria-label="Soft blue paint splash wash"/>

  <g class="brand">
    <circle cx="370" cy="230" r="128" fill="none" stroke="var(--white)" stroke-width="2" opacity=".8"/>
    <circle cx="370" cy="230" r="118" fill="var(--teal-soft)" opacity=".85"/>
    <text class="brand-name" x="372" y="222" text-anchor="middle">PURE</text>
    <text class="brand-name" x="372" y="264" text-anchor="middle">RIDGE</text>
  </g>

  <text class="product-title" x="60" y="540" textLength="440" lengthAdjust="spacingAndGlyphs">Keto Bar</text>
  <path class="title-rule" d="M40 565 Q280 580 520 625" fill="none" stroke="var(--white)" stroke-width="2"/>

  <g class="claims">
    <text class="claim" x="60" y="670">✓ Suitable For A Keto / LCHF Diet,</text>
    <text class="claim" x="60" y="703">✓ 3.5g Net Carbs,</text>
    <text class="claim" x="60" y="736">✓ Vegan</text>
  </g>

  <path d="M30 900 Q30 860 70 860 L490 860 Q530 860 530 900" fill="none" stroke="var(--plum)" stroke-width="2"/>
  <rect x="180" y="846" width="200" height="28" fill="var(--paper)"/>
  <text class="section-label" x="280" y="868" text-anchor="middle">INGREDIENTS</text>

  <rect class="ingredient-band" x="0" y="920" width="560" height="64" fill="var(--teal)"/>
  <g class="ingredient-icons">
    <circle cx="50"  cy="920" r="30" fill="#e3c8a8" stroke="var(--plum)" stroke-width="2" role="img" aria-label="Peanuts illustration"/>
    <circle cx="142" cy="920" r="30" fill="#d9b08a" stroke="var(--plum)" stroke-width="2" role="img" aria-label="Almonds illustration"/>
    <circle cx="234" cy="920" r="30" fill="#a98566" stroke="var(--plum)" stroke-width="2" role="img" aria-label="Coconut illustration"/>
    <circle cx="326" cy="920" r="30" fill="#d6d27e" stroke="var(--plum)" stroke-width="2" role="img" aria-label="Pumpkin seeds illustration"/>
    <circle cx="418" cy="920" r="30" fill="#6b6b6b" stroke="var(--plum)" stroke-width="2" role="img" aria-label="Chia seeds illustration"/>
    <circle cx="510" cy="920" r="30" fill="#8c8c84" stroke="var(--plum)" stroke-width="2" role="img" aria-label="Sunflower seeds illustration"/>
  </g>
  <g class="ingredient-dividers" stroke="var(--white)" stroke-width="1" opacity=".7">
    <line x1="96" y1="955" x2="96" y2="982"/><line x1="188" y1="955" x2="188" y2="982"/>
    <line x1="280" y1="955" x2="280" y2="982"/><line x1="372" y1="955" x2="372" y2="982"/>
    <line x1="464" y1="955" x2="464" y2="982"/>
  </g>
  <g class="ingredient-labels" text-anchor="middle">
    <text class="ingredient-label" x="50"  y="972">PEANUTS</text>
    <text class="ingredient-label" x="142" y="972">ALMONDS</text>
    <text class="ingredient-label" x="234" y="972">COCONUT</text>
    <text class="ingredient-label" x="326" y="965">PUMPKIN</text>
    <text class="ingredient-label" x="326" y="978">SEEDS</text>
    <text class="ingredient-label" x="418" y="972">CHIA</text>
    <text class="ingredient-label" x="510" y="965">SUNFLOWER</text>
    <text class="ingredient-label" x="510" y="978">SEEDS</text>
  </g>

  <text class="flavour" x="280" y="1050" text-anchor="middle">Almond Flavour</text>
</svg>
</body>
</html>
```